Bref créative
The Plumwick Nook, business card
Wedding Industry
Simple
Deborah Anne Valcourt
Owner
278 Thistlemoor Avenue
Dorval, QC H9R 4K7
info@ThePlumwickNook.example
www.ThePlumwickNook.example
Looking for something classy, clean and simple. Please, no frills or floral! Updating my website, so please feel free to use any elements form this url:
http://www.sitehost.example/theplumwicknook/2012
Please do not modify logo (name and icons) but feel free to use tag line to your discretion... please keep same font though... placement doesn't matter.
LOGO
LOGO pdf version

```html
<!DOCTYPE html>
<html lang="en">
<head>
<meta charset="utf-8">
<title>The Plumwick Nook — Business Card</title>
<link rel="stylesheet" href="https://fonts.googleapis.com/css2?family=Raleway:wght@400;500;600&family=Dancing+Script:wght@500&display=swap">
<style>
  :root {
    --page-bg: #ecebee;
    --card-bg: #ffffff;
    --plum: #7a5a9c;
    --plum-soft: #9b80b8;
    --ink: #6b6b70;
    --ink-light: #8c8c92;
    --shadow: rgba(40, 30, 55, 0.14);
  }
  * { box-sizing: border-box; margin: 0; padding: 0; }
  html, body { width: 1200px; height: 646px; overflow: hidden; }
  body {
    background: var(--page-bg);
    font-family: "Raleway", sans-serif;
    color: var(--ink);
    display: flex;
    align-items: center;
    justify-content: center;
    gap: 60px;
  }
  .card {
    position: relative;
    width: 520px;
    height: 297px;
    background: var(--card-bg);
    box-shadow: 0 6px 20px var(--shadow);
    overflow: hidden;
  }

  /* Front */
  .card-front {
    display: flex;
    flex-direction: column;
    align-items: center;
    justify-content: center;
  }
  .brand {
    display: flex;
    align-items: center;
    gap: 12px;
  }
  .brand-mark {
    width: 30px;
    height: 30px;
    background: var(--plum);
  }
  .brand-name {
    font-family: "Raleway", sans-serif;
    font-weight: 500;
    font-size: 34px;
    color: var(--ink);
    letter-spacing: 0.5px;
  }
  .tagline {
    margin-top: 8px;
    font-family: "Dancing Script", cursive;
    font-size: 20px;
    color: var(--plum);
  }

  /* Back */
  .band-vertical {
    position: absolute;
    left: 64px;
    top: 0;
    width: 16px;
    height: 100%;
    background: var(--plum);
  }
  .band-horizontal {
    position: absolute;
    left: 64px;
    right: 0;
    top: 22px;
    height: 10px;
    background: var(--plum);
  }
  .bow {
    position: absolute;
    width: 56px;
    height: 40px;
    background: radial-gradient(circle, var(--plum) 0%, var(--plum-soft) 100%);
    border-radius: 6px;
  }
  .bow-top { left: 44px; top: 8px; }
  .bow-bottom { right: 22px; bottom: 22px; }
  .holder {
    position: absolute;
    right: 40px;
    top: 70px;
    text-align: right;
  }
  .holder-name {
    font-weight: 600;
    font-size: 18px;
    color: var(--plum);
  }
  .holder-role {
    margin-top: 4px;
    font-size: 12px;
    color: var(--ink-light);
  }
  .contact {
    position: absolute;
    left: 104px;
    bottom: 30px;
    font-size: 12px;
    line-height: 1.55;
    color: var(--ink);
    list-style: none;
  }
  .address { margin-bottom: 12px; }
  .contact-line {
    display: flex;
    align-items: center;
    gap: 7px;
  }
  .contact-icon {
    width: 13px;
    height: 13px;
    flex: none;
  }
</style>
</head>
<body>
  <section class="card card-front" aria-label="Business card front">
    <div class="brand">
      <span class="brand-mark"></span>
      <span class="brand-name">The Plumwick Nook</span>
    </div>
    <p class="tagline">favours for every occasion</p>
  </section>

  <section class="card card-back" aria-label="Business card back">
    <div class="band-vertical"></div>
    <div class="band-horizontal"></div>
    <div class="bow bow-top" role="img" aria-label="Purple ribbon bow"></div>
    <div class="bow bow-bottom" role="img" aria-label="Purple ribbon bow"></div>

    <div class="holder">
      <p class="holder-name">Deborah Anne Valcourt</p>
      <p class="holder-role">Owner</p>
    </div>

    <div class="contact">
      <p class="address">278 Thistlemoor Avenue<br>Dorval, QC H9R 4K7</p>
      <p class="contact-line">
        <svg class="contact-icon" viewBox="0 0 16 16"><circle cx="8" cy="8" r="8" fill="#7a5a9c"/><path d="M5.5 4.5l1.5 0 .6 2-1 .8a5 5 0 0 0 2.1 2.1l.8-1 2 .6 0 1.5c-3.5.3-6.3-2.5-6-6z" fill="#fff"/></svg>
        514-555-0142
      </p>
      <p class="contact-line">
        <svg class="contact-icon" viewBox="0 0 16 16"><circle cx="8" cy="8" r="8" fill="#7a5a9c"/><rect x="4" y="5.5" width="8" height="5.5" fill="none" stroke="#fff" stroke-width="1"/><path d="M4 5.5l4 3 4-3" fill="none" stroke="#fff" stroke-width="1"/></svg>
        info@ThePlumwickNook.example
      </p>
      <p class="contact-line">
        <svg class="contact-icon" viewBox="0 0 16 16"><circle cx="8" cy="8" r="8" fill="#7a5a9c"/><circle cx="8" cy="8" r="4" fill="none" stroke="#fff" stroke-width="1"/><path d="M4 8h8M8 4c-2 2.5-2 5.5 0 8M8 4c2 2.5 2 5.5 0 8" fill="none" stroke="#fff" stroke-width="0.8"/></svg>
        www.ThePlumwickNook.example
      </p>
    </div>
  </section>
</body>
</html>
```